Redesign Business Cards, Attached

Please read instructions carefully. If you have any questions send a message before submitting your ONE design. Please redesign attached business cards. Double sided. Use same content and descriptions. Use black, silver, crimson red and gold colors. My only issue with the attached design is the background colors. I like the layout as-is. I can provide the individual pictures on the back side later. Do not submit more than one design. One submission shall include both front and back. Do not submit front and back separately. A second project will be launched to create a matching post card after completion of this.
Industry/Entity Type
see description and attachments.
Contact Information for Business Card
Requirements
Must have
- see description and attachments.
Nice to have
Should not have

```html
<!DOCTYPE html>
<html lang="en">
<head>
<meta charset="utf-8">
<title>Harbor Helm Business Card</title>
<link rel="stylesheet" href="https://fonts.googleapis.com/css2?family=Poppins:wght@400;600;700&family=Fira+Sans:ital,wght@1,400&display=swap">
<style>
  :root {
    --page: #c4c4c4;
    --gold: #cea20c;
    --crimson: #d41438;
    --black: #0b0b0b;
    --ink: #161616;
    --white: #ffffff;
    --silver-light: #f0f1f3;
    --silver-mid: #c9cdd2;
    --silver-dark: #a9aeb4;
    --sea-dark: #1c1f23;
    --sea-mid: #3a4654;
    --sea-light: #7d8a96;
  }
  * { box-sizing: border-box; margin: 0; padding: 0; }
  html, body { width: 1093px; height: 1200px; overflow: hidden; }
  body { background: var(--page); position: relative; font-family: "Poppins", sans-serif; }

  .card { position: absolute; left: 264px; width: 580px; height: 357px; overflow: hidden; }
  .card--front { top: 226px; }
  .card--back { top: 620px; }
  .card__art { position: absolute; inset: 0; width: 100%; height: 100%; }

  .brand { position: absolute; display: flex; align-items: center; gap: 10px; }
  .brand__dot { width: 22px; height: 22px; border-radius: 50%; background: var(--gold); flex: none; }
  .brand__name { font-weight: 700; font-size: 22px; line-height: 1.1; color: var(--white); }
  .card--front .brand { left: 40px; top: 155px; }
  .card--back .brand { left: 78px; top: 58px; }

  .contact { position: absolute; left: 322px; top: 84px; color: var(--ink); }
  .contact__name { color: var(--crimson); font-weight: 700; font-size: 23px; line-height: 1.1; letter-spacing: 0.2px; white-space: nowrap; }
  .contact__role { font-size: 17.5px; line-height: 1.2; white-space: nowrap; }
  .contact__pill {
    position: absolute; left: -4px; top: 92px; width: 223px; height: 38px;
    background: var(--black); border-radius: 19px;
    display: flex; align-items: center; justify-content: center; gap: 6px;
    font-weight: 700; font-size: 17px; color: var(--white); white-space: nowrap;
  }
  .contact__pill .contact__label { color: var(--gold); }
  .contact__line { position: absolute; left: 0; display: flex; align-items: center; gap: 8px; font-size: 15.5px; white-space: nowrap; }
  .contact__line--mail { top: 152px; }
  .contact__line--web { top: 174px; }

  .services { position: absolute; inset: 0; }
  .tile {
    position: absolute; width: 119px; height: 67px;
    transform: skewX(-15deg);
    display: flex; align-items: center; justify-content: center;
  }
  .tile span {
    transform: skewX(15deg);
    font-family: "Fira Sans", sans-serif; font-style: italic; font-size: 14px;
    line-height: 15px; color: var(--white); text-align: center; white-space: nowrap;
  }
  .tile--black { background: var(--black); }
  .tile--gold { background: var(--gold); }
  .services__url {
    position: absolute; left: 0; right: 0; top: 320px; text-align: center;
    font-weight: 700; font-size: 17.5px; color: var(--black);
  }
</style>
</head>
<body>

<section class="card card--front" aria-label="Front of business card">
  <svg class="card__art" viewBox="0 0 580 357" preserveAspectRatio="none">
    <defs>
      <linearGradient id="sea-front" x1="0" y1="0" x2="1" y2="1">
        <stop offset="0" stop-color="#2b2e33"/>
        <stop offset="1" stop-color="#16181b"/>
      </linearGradient>
      <linearGradient id="silver-front" x1="0" y1="0" x2="1" y2="1">
        <stop offset="0" stop-color="var(--silver-light)"/>
        <stop offset="0.5" stop-color="var(--silver-mid)"/>
        <stop offset="0.75" stop-color="var(--silver-light)"/>
        <stop offset="1" stop-color="var(--silver-dark)"/>
      </linearGradient>
    </defs>
    <rect width="340" height="357" fill="url(#sea-front)" role="img" aria-label="Dark photo of a motor boat cutting across open water"/>
    <polygon points="262,0 326,0 275,88 241,34" fill="var(--crimson)"/>
    <polygon points="241,329 275,275 326,357 257,357" fill="var(--crimson)"/>
    <polygon points="326,0 336,0 236,179 336,357 326,357 226,179" fill="var(--gold)"/>
    <polygon points="336,0 580,0 580,357 336,357 236,179" fill="url(#silver-front)"/>
  </svg>

  <div class="brand">
    <span class="brand__dot"></span>
    <span class="brand__name">Harbor<br>Helm</span>
  </div>

  <div class="contact">
    <h1 class="contact__name">DANA R. HOLLOWAY</h1>
    <p class="contact__role">USCG Licensed Captain</p>
    <p class="contact__role">Certified Instructor</p>
    <div class="contact__pill">
      <span class="contact__label">TEXT</span>
      <svg width="15" height="15" viewBox="0 0 24 24" aria-hidden="true"><path d="M6.6 10.8a15.1 15.1 0 0 0 6.6 6.6l2.2-2.2a1 1 0 0 1 1-.25 11.4 11.4 0 0 0 3.6.6 1 1 0 0 1 1 1V20a1 1 0 0 1-1 1A17 17 0 0 1 3 4a1 1 0 0 1 1-1h3.5a1 1 0 0 1 1 1c0 1.25.2 2.45.6 3.6a1 1 0 0 1-.25 1z" fill="none" stroke="var(--crimson)" stroke-width="2"/></svg>
      <span>(555) 014-2290</span>
    </div>
    <p class="contact__line contact__line--mail">
      <svg width="16" height="11" viewBox="0 0 16 11" aria-hidden="true"><rect width="16" height="11" fill="var(--crimson)"/><polyline points="0,0 8,6 16,0" fill="none" stroke="var(--white)" stroke-width="1.5"/></svg>
      hello@harborhelm.com
    </p>
    <p class="contact__line contact__line--web">
      <svg width="16" height="16" viewBox="0 0 16 16" aria-hidden="true"><g fill="none" stroke="var(--crimson)" stroke-width="1.4"><circle cx="8" cy="8" r="7"/><ellipse cx="8" cy="8" rx="3" ry="7"/><line x1="1" y1="8" x2="15" y2="8"/></g></svg>
      www.HarborHelm.com
    </p>
  </div>
</section>

<section class="card card--back" aria-label="Back of business card">
  <svg class="card__art" viewBox="0 0 580 357" preserveAspectRatio="none">
    <defs>
      <linearGradient id="silver-back" x1="0" y1="0" x2="1" y2="1">
        <stop offset="0" stop-color="var(--silver-light)"/>
        <stop offset="0.5" stop-color="var(--silver-mid)"/>
        <stop offset="0.8" stop-color="var(--silver-light)"/>
        <stop offset="1" stop-color="var(--silver-dark)"/>
      </linearGradient>
      <linearGradient id="sea-left" x1="0" y1="0" x2="1" y2="1">
        <stop offset="0" stop-color="#2a3440"/>
        <stop offset="1" stop-color="var(--sea-dark)"/>
      </linearGradient>
      <linearGradient id="sea-right" x1="0" y1="0" x2="1" y2="1">
        <stop offset="0" stop-color="var(--sea-mid)"/>
        <stop offset="0.6" stop-color="var(--sea-light)"/>
        <stop offset="1" stop-color="#56636f"/>
      </linearGradient>
    </defs>
    <rect width="580" height="357" fill="url(#silver-back)"/>
    <polygon points="0,0 344,0 281,94 317,160 317,195 0,195" fill="url(#sea-left)" role="img" aria-label="Photo of dark open water with boat wake"/>
    <polygon points="292,0 334,0 305,43 290,28" fill="var(--crimson)"/>
    <polygon points="334,0 344,0 285,94 323,160 313,160 275,94" fill="var(--gold)"/>
    <polygon points="344,0 580,0 580,198 317,198 317,160 285,94" fill="url(#sea-right)" role="img" aria-label="Photo of a white center-console boat speeding over sunlit water"/>
  </svg>

  <div class="brand">
    <span class="brand__dot"></span>
    <span class="brand__name">Harbor<br>Helm</span>
  </div>

  <div class="services">
    <div class="tile tile--black" style="left:78px;top:163px"><span>Hands-On<br>Boat<br>Training</span></div>
    <div class="tile tile--gold" style="left:203px;top:163px"><span>Introduction<br>to Power<br>boating</span></div>
    <div class="tile tile--black" style="left:328px;top:163px"><span>Precision<br>Docking &amp;<br>Boat Handling</span></div>
    <div class="tile tile--gold" style="left:453px;top:163px"><span>Open Water<br>Boat<br>Handling</span></div>

    <div class="tile tile--gold" style="left:36px;top:241px"><span>Island<br>Anchoring</span></div>
    <div class="tile tile--black" style="left:161px;top:241px"><span>Open Water<br>Advanced<br>Maneuvers</span></div>
    <div class="tile tile--gold" style="left:287px;top:241px"><span>Coastal<br>Navigation</span></div>
    <div class="tile tile--black" style="left:412px;top:241px"><span>Captaining/<br>Piloting Service<br>for Your Outings</span></div>

    <p class="services__url">www.HarborHelm.com</p>
  </div>
</section>

</body>
</html>
```